RTV Engineering Business Card Design

We’re looking for an elegant, clean, and timeless business card design that communicates experience, capability, and reliability.

RTV Engineering was established in 1995 , we are a Government Contracting company providing Professional Services to the Department of Harbor Affairs, Frontier Resilience and the Signals Consortium. Our capabilities include: Acquisition & Program Management; Intelligence & Security Operations; Cyber, IT & Network Operations; Lifecycle Logistics & Asset Readiness; C5ISR Systems Engineering & Sustainment.

We want the card to reflect a straightforward, confident approach to business. The design should feel polished and professional without being flashy or overly corporate.

Design Direction
Clean, sophisticated, and uncluttered
Elegant but understated
Strong typography and thoughtful spacing
A timeless aesthetic rather than something overly trendy
Confident and established, with a sense of substance
Easy to read and practical in a real-world business setting

The overall impression should be: “These are experienced professionals who know what they’re doing, do what they say, and can be relied upon.”

We’re open to creative interpretations. The finished card should feel distinctive through its typography, proportions, layout, and attention to detail rather than through excessive graphics or visual effects.

We’re looking for a design that would make a potential client immediately feel that they’re dealing with a capable, trustworthy, and established company.

Company Colors: Navy and Gold/Yellow (but you do not need to use these colors on the card)
Company Name: RTV Engineering Associates, Inc. (known as RTV Engineering)
Website: rtvengineering-hq.example
Company Logo: Navy & Gold (other variations attached)

```html
<!DOCTYPE html>
<html lang="en">
<head>
<meta charset="utf-8">
<title>RTV Engineering Business Card</title>
<link rel="stylesheet" href="https://fonts.googleapis.com/css2?family=Montserrat:wght@400;500;700;800&display=swap">
<style>
  :root {
    --navy: #1d2a5e;
    --navy-deep: #17194a;
    --gold: #fbe04d;
    --white: #ffffff;
    --ink: #1a1a1a;
    --rule: #c9c9c9;
    --backdrop: #e6e6e6;
  }
  * { box-sizing: border-box; margin: 0; padding: 0; }
  html, body {
    width: 1200px; height: 1200px; overflow: hidden;
    background: var(--backdrop);
    font-family: "Montserrat", sans-serif;
  }
  .sheet {
    position: relative; width: 1200px; height: 1200px;
    display: flex; flex-direction: column; align-items: center; justify-content: center; gap: 60px;
  }
  .card {
    position: relative; width: 840px; height: 480px;
    border-radius: 36px; overflow: hidden;
    box-shadow: 0 8px 24px rgba(0,0,0,0.18);
  }
  /* Front */
  .card--front { background: var(--white); }
  .wordmark {
    position: absolute; top: 96px; left: 0; width: 100%;
    text-align: center;
    font-weight: 800; font-size: 54px; letter-spacing: 0.5px;
    color: var(--navy);
  }
  .identity { position: absolute; left: 118px; top: 300px; }
  .identity__name {
    font-weight: 700; font-size: 42px; color: var(--navy); line-height: 1;
  }
  .identity__title {
    font-weight: 400; font-size: 24px; color: var(--ink); margin-top: 6px; letter-spacing: 0.5px;
  }
  .divider {
    position: absolute; left: 472px; top: 270px; width: 1px; height: 120px;
    background: var(--rule);
  }
  .contact { position: absolute; left: 500px; top: 262px; list-style: none; }
  .contact__item {
    display: flex; align-items: center; gap: 12px;
    font-size: 20px; font-weight: 400; color: var(--ink);
    margin-bottom: 14px;
  }
  .contact__item svg { width: 22px; height: 22px; flex: none; }
  .band { position: absolute; bottom: 0; height: 26px; }
  .band--gold { left: 0; width: 520px; background: var(--gold); }
  .band--navy { left: 532px; right: 0; height: 34px; background: var(--navy); }
  /* Back */
  .card--back {
    background: var(--navy-deep);
    display: flex; align-items: center; justify-content: center;
    border-bottom: 3px solid var(--gold);
  }
  .wordmark--reverse {
    position: static; width: auto;
    color: var(--white); font-size: 64px;
  }
</style>
</head>
<body>
<main class="sheet">
  <section class="card card--front" aria-label="Business card front">
    <div class="wordmark">RTV Engineering</div>
    <div class="identity">
      <p class="identity__name">FULL NAME</p>
      <p class="identity__title">TITLE</p>
    </div>
    <div class="divider"></div>
    <ul class="contact">
      <li class="contact__item">
        <svg viewBox="0 0 24 24" aria-hidden="true"><path fill="#1d2a5e" d="M6.6 10.8a15.1 15.1 0 0 0 6.6 6.6l2.2-2.2a1 1 0 0 1 1-.25 11.4 11.4 0 0 0 3.6.6 1 1 0 0 1 1 1V20a1 1 0 0 1-1 1A17 17 0 0 1 3 4a1 1 0 0 1 1-1h3.5a1 1 0 0 1 1 1c0 1.25.2 2.45.6 3.6a1 1 0 0 1-.25 1z"/></svg>
        (000) 000 0000
      </li>
      <li class="contact__item">
        <svg viewBox="0 0 24 24" aria-hidden="true"><rect x="2" y="5" width="20" height="14" fill="#1d2a5e"/><path d="M2 5l10 8 10-8" fill="none" stroke="#fff" stroke-width="1.6"/></svg>
        hello@rtvengineering-hq.example
      </li>
      <li class="contact__item">
        <svg viewBox="0 0 24 24" aria-hidden="true"><g fill="none" stroke="#1d2a5e" stroke-width="1.8"><circle cx="12" cy="12" r="9.5"/><ellipse cx="12" cy="12" rx="4" ry="9.5"/><path d="M2.5 12h19M4 7h16M4 17h16"/></g></svg>
        www.rtvengineering-hq.example
      </li>
    </ul>
    <div class="band band--gold"></div>
    <div class="band band--navy"></div>
  </section>

  <section class="card card--back" aria-label="Business card back">
    <div class="wordmark wordmark--reverse">RTV Engineering</div>
  </section>
</main>
</body>
</html>
```